Real Estate Company needs Stationary.
Business Cards, Letterhead, Envelope Stationary etc...
Real Estate Company needs Stationary. -
Creative Brief
Professional
Tomas Velbrik
Broker
3871 W. Marrowfield Ave., Suite K-214 Marrowfield TX, 75318
1 (866) 514-VKOR (5867)
tomas@vkorhomesllc.example
www.vkorhomesllc.example
We are a real estate company looking for a slick contemporary design. Use logo in the design. Use logo colors if desired. Would like Business cards, Letterhead, and Envelope. I would like all the stationary items to carry the same theme my logo protrays. Email me with questions.
I would like the logo on back, and open to any other sugestions.

```html
<!DOCTYPE html>
<html lang="en">
<head>
<meta charset="utf-8">
<title>vKorHomes Presentation Folder</title>
<link href="https://fonts.googleapis.com/css2?family=Arimo:wght@400;700&display=swap" rel="stylesheet">
<style>
  :root {
    --green-deep: #2f9a3a;
    --green-light: #a6d34a;
    --blue-deep: #1a56a8;
    --blue-light: #4a9ae0;
    --paper: #ffffff;
    --edge: #c9c9c9;
    --ink-green: #3b9a3f;
    --ink-blue: #1f5eb0;
  }
  html, body {
    margin: 0;
    padding: 0;
    width: 1200px;
    height: 1059px;
    overflow: hidden;
    background: var(--paper);
    font-family: "Arimo", Arial, sans-serif;
  }
  .folder { display: block; width: 1200px; height: 1059px; }
  .panel { fill: var(--paper); stroke: var(--edge); stroke-width: 1.5; }
  .brand-back { font-weight: 700; font-size: 22px; fill: var(--ink-blue); }
  .contact { font-size: 10px; fill: var(--ink-green); }
  .contact-web { font-size: 10px; fill: var(--ink-blue); font-weight: 700; }
  .brand-front { font-weight: 700; font-size: 50px; fill: var(--ink-blue); }
  .card-name { font-weight: 700; font-size: 10px; fill: var(--ink-blue); }
  .card-line { font-size: 6px; fill: #ffffff; }
  .card-role { font-size: 7px; fill: var(--ink-green); }
</style>
</head>
<body>
<svg class="folder" viewBox="0 0 1200 1059" xmlns="http://www.w3.org/2000/svg">
  <defs>
    <linearGradient id="greenSheen" x1="0" x2="1" y1="0" y2="0">
      <stop offset="0" stop-color="var(--green-deep)"/>
      <stop offset="0.5" stop-color="var(--green-light)"/>
      <stop offset="1" stop-color="var(--green-deep)"/>
    </linearGradient>
    <linearGradient id="blueSheen" x1="0" x2="1" y1="0" y2="0">
      <stop offset="0" stop-color="var(--blue-deep)"/>
      <stop offset="0.5" stop-color="var(--blue-light)"/>
      <stop offset="1" stop-color="var(--blue-deep)"/>
    </linearGradient>
  </defs>

  <!-- back cover -->
  <g class="back-cover">
    <rect class="panel" x="43" y="14" width="545" height="801"/>
    <rect x="302" y="560" width="26" height="26" fill="var(--ink-green)"/>
    <text class="brand-back" x="315" y="620" text-anchor="middle">vKorHomes</text>
    <text class="contact" x="315" y="664" text-anchor="middle">3871 W. Marrowfield Ave., Suite K-214 Marrowfield TX, 75318</text>
    <text class="contact" x="315" y="680" text-anchor="middle">T: 1 (866) 514-VKOR (5867)  P: (866) 514-2200  F: (866) 514-3390</text>
    <text class="contact-web" x="315" y="696" text-anchor="middle">www.vkorhomesllc.example</text>
  </g>

  <!-- front cover -->
  <g class="front-cover">
    <rect class="panel" x="591" y="14" width="566" height="801"/>
    <path d="M591 14 H1157 V470 C1000 520 850 590 591 570 Z" fill="url(#greenSheen)"/>
    <path d="M591 570 C850 590 1000 520 1157 470 L1157 492 C1000 545 850 612 591 592 Z" fill="url(#blueSheen)"/>
    <rect x="868" y="600" width="64" height="64" fill="var(--ink-green)"/>
    <text class="brand-front" x="900" y="730" text-anchor="middle">vKorHomes</text>
  </g>

  <!-- pockets -->
  <path class="pocket pocket-left" d="M43 815 H588 V990 L577 1001 H55 L43 990 Z" fill="url(#blueSheen)"/>
  <path class="pocket pocket-right" d="M591 815 H1157 V990 L1146 1001 H603 L591 990 Z" fill="url(#blueSheen)"/>
  <path d="M588 815 L604 852 L588 852 Z" fill="var(--paper)"/>

  <!-- business card in slot (upside down) -->
  <g class="business-card" transform="rotate(180 850 894)">
    <rect x="757" y="830" width="186" height="128" fill="var(--paper)" stroke="var(--edge)"/>
    <rect x="757" y="830" width="186" height="52" fill="url(#greenSheen)"/>
    <path d="M757 882 C830 890 880 876 943 866 V874 C880 886 830 898 757 890 Z" fill="var(--ink-blue)"/>
    <text class="card-line" x="765" y="846">1 (866) 514-VKOR (5867)</text>
    <text class="card-line" x="765" y="856">tomas@vkorhomesllc.example</text>
    <text class="card-line" x="765" y="866">www.vkorhomesllc.example</text>
    <rect x="843" y="900" width="14" height="14" fill="var(--ink-green)"/>
    <text class="card-name" x="850" y="930" text-anchor="middle">Tomas Velbrik</text>
    <text class="card-role" x="850" y="942" text-anchor="middle">Broker</text>
  </g>
</svg>
</body>
</html>
```